Educate
Education
Creative Brief
It an educational site, N.G.O
Likes: Green White Green
above header
http://brevardlearning.org/
http://www.koltrex.org/offices/education/about/index.html

```html
<!DOCTYPE html>
<html lang="en">
<head>
<meta charset="utf-8">
<title>Brightpath Learning</title>
<link rel="stylesheet" href="https://fonts.googleapis.com/css2?family=Arimo:wght@400;700&display=swap">
<style>
  :root {
    --green-dark: #1f7a12;
    --green: #3a9a22;
    --green-mid: #4fae2c;
    --green-light: #7ccb4f;
    --green-pale: #e4f3da;
    --white: #ffffff;
    --ink: #222222;
    --muted: #6b6b6b;
    --photo-warm: #a9866a;
    --photo-dark: #5a4636;
  }
  * { box-sizing: border-box; margin: 0; padding: 0; }
  html, body { width: 1200px; height: 670px; overflow: hidden; background: var(--white); }
  body { position: relative; font-family: "Arimo", Arial, sans-serif; color: var(--ink); }

  .brand {
    position: absolute; left: 84px; top: 52px;
    display: flex; align-items: center; gap: 12px;
  }
  .brand-mark { width: 34px; height: 34px; border-radius: 50%; background: var(--green); }
  .brand-name {
    font-size: 30px; font-weight: 700; color: var(--green-dark); letter-spacing: 1px; line-height: 1;
  }

  .header-rule {
    position: absolute; left: 0; top: 134px; width: 1200px; height: 10px;
    background: linear-gradient(to right, var(--white) 0%, var(--green-light) 30%, var(--green) 100%);
  }

  .main-nav { position: absolute; left: 372px; top: 84px; display: flex; gap: 7px; }
  .main-nav a {
    display: flex; align-items: center; justify-content: center;
    height: 54px; font-size: 18px; text-decoration: none; color: var(--white);
    background: linear-gradient(to bottom, var(--green-mid), var(--green-dark));
    border-radius: 4px 4px 0 0;
  }
  .main-nav a.is-active {
    color: var(--green-dark);
    background: linear-gradient(to bottom, var(--white), var(--green-pale));
  }

  .content-panel {
    position: absolute; left: 65px; top: 144px; width: 1068px; height: 473px;
    background: linear-gradient(to bottom, var(--green-mid), var(--green-dark));
    border-radius: 0 0 14px 14px;
  }

  .hero {
    position: absolute; left: 86px; top: 163px; width: 687px; height: 300px;
    border: 5px solid var(--white); border-radius: 6px; overflow: hidden;
    background: linear-gradient(135deg, var(--photo-dark), var(--photo-warm) 55%, #c9a98a);
  }
  .hero-title {
    position: absolute; left: 10px; top: 12px;
    font-size: 27px; font-weight: 700; color: var(--white);
  }
  .hero-dots { position: absolute; right: 14px; bottom: 10px; display: flex; gap: 5px; }
  .hero-dots span { width: 14px; height: 14px; background: rgba(255,255,255,0.6); }
  .hero-dots span.is-current { background: var(--green-light); }

  .sidebar { position: absolute; left: 792px; top: 163px; width: 319px; }
  .sidebar-bar {
    height: 36px; padding: 0 14px; display: flex; align-items: center; justify-content: space-between;
    font-size: 17px; color: var(--white);
    background: linear-gradient(to bottom, var(--green-light), var(--green));
    border: 2px solid var(--white); border-radius: 4px;
  }
  .sidebar-bar svg { width: 16px; height: 16px; }
  .announcements { background: var(--white); padding: 12px 10px 6px; height: 178px; }
  .announce-item { display: flex; gap: 10px; margin-bottom: 14px; }
  .announce-thumb {
    width: 72px; height: 60px; flex: none; border: 2px solid #ddd;
    background: linear-gradient(135deg, #7a5b45, #c8a68c);
  }
  .announce-item h3 { font-size: 14px; font-weight: 700; margin-top: 4px; }
  .announce-item p { font-size: 12px; color: var(--muted); line-height: 1.3; }
  .see-all { display: block; text-align: right; font-size: 13px; color: var(--green-dark); text-decoration: none; }
  .sidebar .sidebar-bar + .sidebar-bar, .announcements + .sidebar-bar { margin-top: 4px; }

  .feature-card {
    position: absolute; top: 480px; height: 120px;
    border: 4px solid var(--white); border-radius: 4px; overflow: hidden;
  }
  .feature-photo { position: absolute; inset: 0; }
  .feature-caption {
    position: absolute; left: 0; right: 0; bottom: 0; height: 52px; padding: 8px 12px;
    background: rgba(255,255,255,0.85);
  }
  .feature-caption h2 { font-size: 14px; font-weight: 700; color: var(--green-dark); }
  .feature-caption p { font-size: 14px; color: var(--ink); }

  .site-footer {
    position: absolute; left: 72px; right: 72px; top: 627px; height: 22px;
    display: flex; align-items: center; justify-content: space-between; font-size: 12px; color: var(--ink);
  }
  .footer-links { display: flex; align-items: center; gap: 8px; }
  .footer-links .dot { width: 14px; height: 14px; border-radius: 50%; background: var(--green-light); }
  .footer-links .square { width: 40px; height: 14px; background: #e8822a; margin-left: 24px; }
</style>
</head>
<body>
  <header>
    <div class="brand">
      <span class="brand-mark"></span>
      <span class="brand-name">BRIGHTPATH LEARNING</span>
    </div>
    <nav class="main-nav">
      <a href="#" class="is-active" style="width:168px">Home</a>
      <a href="#" style="width:125px">About Us</a>
      <a href="#" style="width:161px">Educations</a>
      <a href="#" style="width:161px">News &amp; Events</a>
      <a href="#" style="width:118px">Contact Us</a>
    </nav>
    <div class="header-rule"></div>
  </header>

  <main>
    <div class="content-panel"></div>

    <section class="hero" role="img" aria-label="Photo of children dancing together in a classroom">
      <h1 class="hero-title">Working together to create a community of...</h1>
      <div class="hero-dots"><span class="is-current"></span><span></span><span></span><span></span></div>
    </section>

    <aside class="sidebar">
      <div class="sidebar-bar">Announcements
        <svg viewBox="0 0 16 16"><path d="M3 5l5 6 5-6" fill="none" stroke="#fff" stroke-width="2.5"/></svg>
      </div>
      <div class="announcements">
        <div class="announce-item">
          <div class="announce-thumb" role="img" aria-label="Portrait thumbnail of a student"></div>
          <div><h3>Lorem ipsum dolor sit amet,</h3><p>Consectetur adipiscing elit, sed do eiusmod tempor incididunt</p></div>
        </div>
        <div class="announce-item">
          <div class="announce-thumb" role="img" aria-label="Portrait thumbnail of a student"></div>
          <div><h3>Lorem ipsum dolor sit amet,</h3><p>Consectetur adipiscing elit, sed do eiusmod tempor incididunt</p></div>
        </div>
        <a href="#" class="see-all">See All »</a>
      </div>
      <div class="sidebar-bar">Informations
        <svg viewBox="0 0 16 16"><path d="M3 11l5-6 5 6" fill="none" stroke="#fff" stroke-width="2.5"/></svg>
      </div>
      <div class="sidebar-bar">News &amp; Events
        <svg viewBox="0 0 16 16"><path d="M3 11l5-6 5 6" fill="none" stroke="#fff" stroke-width="2.5"/></svg>
      </div>
    </aside>

    <article class="feature-card" style="left:86px;width:346px">
      <div class="feature-photo" role="img" aria-label="Photo of a smiling child beside a chalkboard" style="background:linear-gradient(90deg,#6b5444,#9a8878 50%,#c9c2b8)"></div>
      <div class="feature-caption"><h2>2010 PROGRAMS</h2><p>See Our Programs at 2010</p></div>
    </article>
    <article class="feature-card" style="left:446px;width:327px">
      <div class="feature-photo" role="img" aria-label="Photo of students in colourful clothing at school" style="background:linear-gradient(90deg,#5b7d8a,#b07a86 50%,#7a6a58)"></div>
      <div class="feature-caption"><h2>EDUCATIONS</h2><p>See Our Educations here</p></div>
    </article>
    <article class="feature-card" style="left:792px;width:319px">
      <div class="feature-photo" role="img" aria-label="Photo of a girl wearing a headscarf" style="background:linear-gradient(90deg,#b88a52,#d9a86a 50%,#8c6440)"></div>
      <div class="feature-caption"><h2>DONATE NOW</h2><p>Support Brightpath Learning</p></div>
    </article>
  </main>

  <footer class="site-footer">
    <span>© Copyright 2010 BRIGHTPATH LEARNING &nbsp; Allright Reserved</span>
    <div class="footer-links">
      <span class="dot"></span><span>Chirper</span>
      <span class="square"></span><span>Subscribe</span>
    </div>
  </footer>
</body>
</html>
```